Builders Worksite Corflute Outdoor Sign

We are a building company who are just branching out into new construction. How first new build is our own home which was designed by us and a local architect. We are proud and want to create more advertisement around our business.

We need a corflute sign that can staked outside the construction site and can be seen by people passing by.
Updates

Can we please make the company name and logo bigger (Tidewater Lane Homes) This needs to be the focus. Can we please replace 'Mako' with 'Contact Us on 021-649-3157'

Target Market(s)

Home owners and people wishing to build on lifestyle blocks in New Zealand.

Font styles to use
Sans Serif

Requirements
Must have
• It needs to feature our:
Logo
Company name
Contact name and number - Mako - 0216493157
Landscape NOT portrait.

```html
<!DOCTYPE html>
<html lang="en">
<head>
<meta charset="utf-8">
<title>Tidewater Lane Homes – Worksite Sign</title>
<link rel="stylesheet" href="https://fonts.googleapis.com/css2?family=Questrial&family=Poppins:wght@600&display=swap">
<style>
  :root {
    --paper: #ffffff;
    --navy: #1a2130;
    --gold: #f4c116;
    --gold-deep: #d9a800;
    --white: #ffffff;
  }
  html, body {
    margin: 0;
    padding: 0;
    width: 1200px;
    height: 900px;
    overflow: hidden;
    background: var(--paper);
  }
  .canvas {
    position: relative;
    width: 1200px;
    height: 900px;
  }
  .sign {
    position: absolute;
    left: 253px;
    top: 197px;
    width: 720px;
    height: 480px;
    box-shadow: 0 0 6px rgba(0, 0, 0, 0.18);
  }
  .sign svg {
    display: block;
  }
  .brand-name {
    font-family: "Questrial", "Century Gothic", sans-serif;
    fill: var(--navy);
  }
  .brand-sub {
    font-family: "Questrial", "Century Gothic", sans-serif;
    fill: var(--navy);
  }
  .ribbon-label {
    font-family: "Poppins", "Century Gothic", sans-serif;
    font-weight: 600;
    fill: var(--white);
  }
  .phone-number {
    font-family: "Questrial", "Century Gothic", sans-serif;
    fill: var(--gold);
  }
</style>
</head>
<body>
<main class="canvas">
  <section class="sign" aria-label="Tidewater Lane Homes worksite sign">
    <svg width="720" height="480" viewBox="0 0 720 480" xmlns="http://www.w3.org/2000/svg">
      <rect class="sign-face" x="0" y="0" width="720" height="480" fill="var(--paper)"/>

      <polygon class="top-band" points="157,0 579,0 563,23 175,23" fill="var(--gold)"/>

      <text class="brand-name" x="360" y="152" text-anchor="middle" font-size="70" textLength="660" lengthAdjust="spacingAndGlyphs">TIDEWATER LANE</text>
      <text class="brand-sub" x="368" y="231" text-anchor="middle" font-size="60" letter-spacing="34">HOMES</text>

      <rect class="contact-panel" x="0" y="296" width="720" height="184" fill="var(--navy)"/>

      <polygon class="ribbon-fold" points="136,296 156,268 169,296" fill="var(--gold-deep)"/>
      <polygon class="ribbon-fold" points="581,268 602,296 570,296" fill="var(--gold-deep)"/>
      <polygon class="ribbon" points="156,268 581,268 557,330 184,330" fill="var(--gold)"/>

      <text class="ribbon-label" x="369" y="316" text-anchor="middle" font-size="44" textLength="347" lengthAdjust="spacingAndGlyphs">CONTACT US ON</text>

      <text class="phone-number" x="361" y="432" text-anchor="middle" font-size="90" textLength="546" lengthAdjust="spacingAndGlyphs">021-649-3157</text>
    </svg>
  </section>
</main>
</body>
</html>
```